Book cover for The Quiet Harbor Method to Grow a Fearless Venture

Book cover design for soft cover non-fiction book.

The front cover is what is most important at this stage, I am still gathering the testimonials and book description for the back cover so a rough to be completed later for the back is great.

Title as per above. Divided up "The Quiet Harbor Method" (to be a series) and "Grow a Fearless Venture" in this book in the series

Also for the front:

Corla Vennick

"The most unusual business book you will read." - Jodi Marquenthal, Author of Founder Tidewalk

Background info:

This work is a blending of the masculine and feminine energies, the practical business skills with a strong focus on the inner game. I am looking for the cover to have a nod to the Dominatrix and a clear message that one can be soft (kind, open hearted) and still be strong and firm in business.

Photo options are in this file https://www.filecrate-share.example/sh/qk41mxw07trbvle/BBFupdmWqYrLs3NxKeei47K5b?dl=0

Size 6" x 9" 179 pgs

Target Market(s)

female entreprenures

Industry/Entity Type

Business

Colors

Designer to choose colors to be used in the design.

Requirements
Must have
• I would like the title to be in a font that is bold and upscale, to contrast the softness fo the image.
• Clear and readable
• Unique look that will stand out
Should not have
• overt Dominatrix images or slant. It is about the energy not the actual.

```html
<!DOCTYPE html>
<html lang="en">
<head>
<meta charset="utf-8">
<title>The Quiet Harbor Method – Cover Spread</title>
<link rel="stylesheet" href="https://fonts.googleapis.com/css2?family=Cormorant+SC:wght@500;600&family=Cormorant+Garamond:wght@500&family=Great+Vibes&display=swap">
<style>
  :root {
    --backdrop-dark: #6e6e6e;
    --backdrop-light: #ffffff;
    --harbor-blue: #3f6d94;
    --spine-blue: #4e7899;
    --mist: #dde2ea;
    --blush: #cfb2b9;
    --wine: #8a5560;
    --ink: #141414;
    --paper: #ffffff;
    --serif-caps: "Cormorant SC", "Times New Roman", serif;
    --serif: "Cormorant Garamond", "Times New Roman", serif;
    --script: "Great Vibes", cursive;
  }
  * { box-sizing: border-box; margin: 0; padding: 0; }
  html, body { width: 1200px; height: 1200px; overflow: hidden; }
  body {
    position: relative;
    background: linear-gradient(90deg, var(--backdrop-dark) 0%, #b8b8b8 45%, var(--backdrop-light) 100%);
    font-family: var(--serif-caps);
  }
  .spread { position: absolute; left: 0; top: 198px; width: 1200px; height: 800px; }
  .back-cover, .front-cover { position: absolute; top: 0; height: 800px; overflow: hidden; }
  .back-cover {
    left: 0; width: 564px;
    background:
      radial-gradient(ellipse 260px 200px at 120px 110px, rgba(63,109,148,.85), transparent 70%),
      radial-gradient(ellipse 220px 160px at 470px 80px, rgba(138,85,96,.55), transparent 70%),
      radial-gradient(ellipse 300px 240px at 300px 420px, rgba(221,226,234,.95), transparent 70%),
      radial-gradient(ellipse 260px 200px at 500px 700px, rgba(63,109,148,.65), transparent 70%),
      radial-gradient(ellipse 240px 200px at 60px 620px, rgba(207,178,185,.8), transparent 70%),
      linear-gradient(160deg, #6f8fac 0%, var(--mist) 45%, #b9c3d0 100%);
  }
  .front-cover {
    left: 640px; width: 560px;
    background:
      radial-gradient(ellipse 240px 180px at 120px 60px, rgba(63,109,148,.6), transparent 70%),
      radial-gradient(ellipse 260px 220px at 480px 220px, rgba(207,178,185,.85), transparent 70%),
      radial-gradient(ellipse 280px 220px at 120px 560px, rgba(138,85,96,.55), transparent 70%),
      radial-gradient(ellipse 320px 220px at 420px 760px, rgba(63,109,148,.9), transparent 70%),
      radial-gradient(ellipse 200px 160px at 80px 760px, rgba(63,109,148,.8), transparent 70%),
      linear-gradient(170deg, var(--mist) 0%, #e6d9dd 40%, #a9b6c6 100%);
  }
  .spine { position: absolute; left: 564px; top: 0; width: 76px; height: 800px; background: var(--spine-blue); }
  .spine-title {
    position: absolute; left: 50%; top: 50%;
    transform: translate(-50%, -50%) rotate(-90deg);
    white-space: nowrap;
    font-family: var(--script); font-size: 58px; color: var(--paper);
  }

  .blurb-lead {
    position: absolute; color: var(--paper); font-weight: 600;
    font-size: 27px; line-height: 1; letter-spacing: .5px; white-space: nowrap;
    text-shadow: 0 1px 3px rgba(0,0,0,.35);
  }
  .blurb-lead.l1 { left: 36px; top: 50px; }
  .blurb-lead.l2 { left: 144px; top: 80px; }
  .blurb-lead.l3 { left: 221px; top: 112px; font-size: 22px; }
  .back-note {
    position: absolute; font-family: var(--serif); font-size: 18px; line-height: 1;
    font-weight: 500; letter-spacing: .5px; white-space: nowrap;
  }
  .back-note.light { color: var(--paper); }
  .back-note.n1 { left: 50px; top: 190px; }
  .back-note.n2 { left: 74px; top: 220px; }
  .back-note.n3 { left: 100px; top: 434px; color: var(--ink); }
  .back-author {
    position: absolute; right: 15px; top: 740px;
    font-size: 26px; font-weight: 600; color: var(--ink); letter-spacing: .5px;
  }

  .series-name {
    position: absolute; left: 0; width: 565px; top: 28px; text-align: center;
    font-size: 30px; font-weight: 600; color: var(--ink); letter-spacing: .5px;
  }
  .book-subtitle {
    position: absolute; left: 0; width: 565px; top: 64px; text-align: center;
    font-size: 23px; font-weight: 600; color: var(--ink); letter-spacing: .5px;
  }
  .figure-art { position: absolute; left: 16px; top: 130px; width: 260px; height: 590px; }
  .author-name {
    position: absolute; right: 18px; top: 186px;
    font-size: 29px; font-weight: 600; color: var(--ink); letter-spacing: .5px;
  }
  .author-credit {
    position: absolute; right: 26px; top: 219px;
    font-size: 13px; font-weight: 600; color: var(--ink); letter-spacing: .3px;
  }
  .main-title {
    position: absolute; font-family: var(--script); color: var(--paper);
    line-height: 1; white-space: nowrap; text-align: right;
    font-size: 104px;
    text-shadow: 2px 2px 3px rgba(60,70,90,.55);
  }
  .main-title.w1 { right: 116px; top: 262px; font-size: 120px; }
  .main-title.w2 { right: 40px; top: 384px; }
  .main-title.w3 { right: 36px; top: 496px; }
  .main-title.w4 { right: 76px; top: 610px; }
</style>
</head>
<body>
  <div class="spread">
    <section class="back-cover">
      <p class="blurb-lead l1">The most Unusual</p>
      <p class="blurb-lead l2">Business Book</p>
      <p class="blurb-lead l3">you will read</p>
      <p class="back-note light n1">Grow a Fearless Venture</p>
      <p class="back-note light n2">More info goes here...</p>
      <p class="back-note n3">More texts goes here...?</p>
      <p class="back-author">Jodi Marquenthal</p>
    </section>

    <section class="spine">
      <p class="spine-title">The Quiet Harbor Method</p>
    </section>

    <section class="front-cover">
      <p class="series-name">The Quiet Harbor Method</p>
      <p class="book-subtitle">Grow a Fearless Venture</p>
      <svg class="figure-art" viewBox="0 0 260 590" role="img" aria-label="Fashion illustration of a woman in a blue coat holding a riding crop">
        <defs>
          <linearGradient id="figureTone" x1="0" y1="0" x2="0" y2="1">
            <stop offset="0" stop-color="#3f6d94" stop-opacity="0"/>
            <stop offset="0.2" stop-color="#3f6d94" stop-opacity=".55"/>
            <stop offset="0.6" stop-color="#2f5878" stop-opacity=".55"/>
            <stop offset="1" stop-color="#1c1c1c" stop-opacity=".15"/>
          </linearGradient>
        </defs>
        <rect x="0" y="0" width="260" height="590" rx="40" fill="url(#figureTone)"/>
      </svg>
      <p class="author-name">Jodi Marquenthal</p>
      <p class="author-credit">Author of Founder Tidewalk</p>
      <p class="main-title w1">The</p>
      <p class="main-title w2">Quiet</p>
      <p class="main-title w3">Harbor</p>
      <p class="main-title w4">Method</p>
    </section>
  </div>
</body>
</html>
```